Visitenkarten-Design für Styling-Coach
Zielgruppe
Styling Coach
Aufgabenstellung
Colors, Logo, Two side design, one side with Information/Logo other backside nice design
Info Card Front:
Helene Sofia Krantz
Lindenhof 27
8847 Talberg
krantz@krantzstyling.example
www.krantzstyling.example

```html
<!DOCTYPE html>
<html lang="de">
<head>
<meta charset="utf-8">
<title>Helene Sofia Krantz – Styling Coach Visitenkarte</title>
<link rel="stylesheet" href="https://fonts.googleapis.com/css2?family=Open+Sans:wght@400;600;700&display=swap">
<style>
  :root {
    --page-bg: #ece9e6;
    --card-pink: #f0bcd4;
    --card-mid: #ddd6d4;
    --card-mint: #c6e5d3;
    --accent-pink: #d9549c;
    --accent-soft: #e58bbb;
    --ink: #111111;
    --card-shadow: rgba(0, 0, 0, 0.18);
  }
  * { margin: 0; padding: 0; box-sizing: border-box; }
  html, body {
    width: 1200px;
    height: 900px;
    overflow: hidden;
    background: var(--page-bg);
    font-family: "Open Sans", Arial, sans-serif;
    color: var(--ink);
  }
  .canvas {
    width: 1200px;
    height: 900px;
    display: flex;
    flex-direction: column;
    align-items: center;
    justify-content: center;
    gap: 40px;
  }
  .card {
    position: relative;
    width: 700px;
    height: 400px;
    background: linear-gradient(90deg, var(--card-pink) 0%, var(--card-mid) 50%, var(--card-mint) 100%);
    box-shadow: 0 6px 18px var(--card-shadow);
    overflow: hidden;
  }

  /* Logo side */
  .brand {
    position: absolute;
    left: 90px;
    top: 150px;
    display: flex;
    align-items: center;
    gap: 22px;
  }
  .brand-dot {
    width: 64px;
    height: 64px;
    border-radius: 50%;
    background: var(--accent-pink);
    flex: none;
  }
  .brand-text {
    font-weight: 600;
    color: var(--ink);
  }
  .brand-name {
    font-size: 31px;
    letter-spacing: 1px;
    line-height: 1.25;
  }
  .brand-role {
    font-size: 31px;
    letter-spacing: 12px;
    line-height: 1.35;
  }

  /* Info side */
  .motif-area {
    position: absolute;
    left: 70px;
    top: 0;
    width: 200px;
    height: 400px;
    background: linear-gradient(90deg, var(--accent-soft) 0%, var(--accent-pink) 100%);
    opacity: 0.85;
  }
  .contact {
    position: absolute;
    left: 330px;
    top: 95px;
    font-size: 21px;
    line-height: 1.2;
  }
  .contact-name {
    font-weight: 700;
    font-size: 23px;
    margin-bottom: 12px;
  }
  .contact-group { margin-bottom: 12px; }
  .contact-web {
    font-weight: 700;
    font-size: 23px;
  }
</style>
</head>
<body>
<main class="canvas">
  <section class="card card-logo-side" aria-label="Vorderseite mit Markenname">
    <div class="brand">
      <span class="brand-dot" aria-hidden="true"></span>
      <div class="brand-text">
        <p class="brand-name">HELENE SOFIA KRANTZ</p>
        <p class="brand-role">STYLING COACH</p>
      </div>
    </div>
  </section>

  <section class="card card-info-side" aria-label="Rückseite mit Kontaktdaten">
    <div class="motif-area" role="img" aria-label="Fläche für das große dekorative Markenmotiv in Pink"></div>
    <div class="contact">
      <p class="contact-name">Helene Sofia Krantz</p>
      <div class="contact-group">
        <p>Lindenhof 27</p>
        <p>8847 Talberg</p>
      </div>
      <div class="contact-group">
        <p>+41 44 555 0172</p>
        <p>+41 79 555 0148</p>
      </div>
      <div class="contact-group">
        <p>krantz@krantzstyling.example</p>
      </div>
      <p class="contact-web">www.krantzstyling.example</p>
    </div>
  </section>
</main>
</body>
</html>
```